Potential SF Gazette Best Seller Poetry Book Cover Contest

I’m penning my first poetry book. It’s entitled “Lanterns Under Rain”
I’m fairly open to creative freedom but I want the cover to without a doubt catch a persons' eye instantly because first impressions are VERY IMPORTANT in the literary world
I tend to lean towards a luxury look and colors like black, gold, rose gold, silver, glitter etc but again I’m open to interpretation
Looking forward to your submissions
Target Market(s)
those seeking relatable love advice and quotes
modern millenials
Colors
Look and feel

```html
<!DOCTYPE html>
<html lang="en">
<head>
<meta charset="UTF-8">
<title>Lanterns Under Rain — Book Cover</title>
<link rel="stylesheet" href="https://fonts.googleapis.com/css2?family=Archivo+Black&family=Tinos&family=Lato:wght@300&display=swap">
<style>
  :root {
    --rose: #b86e79;
    --ink: #000000;
    --paper: #ffffff;
    --gold: #fdc514;
  }
  html, body {
    margin: 0;
    padding: 0;
    width: 900px;
    height: 1200px;
    overflow: hidden;
    background: var(--ink);
  }
  .cover {
    position: relative;
    width: 900px;
    height: 1200px;
    background: var(--ink);
    overflow: hidden;
  }
  .cover-art {
    position: absolute;
    inset: 0;
    width: 900px;
    height: 1200px;
    display: block;
  }
  .title-line {
    font-family: "Archivo Black", "Arial Black", sans-serif;
    fill: var(--paper);
  }
  .title-word {
    font-family: "Archivo Black", "Arial Black", sans-serif;
    fill: var(--rose);
  }
  .author {
    position: absolute;
    left: 48px;
    top: 1100px;
    margin: 0;
    font-family: "Tinos", "Times New Roman", serif;
    font-size: 36px;
    font-weight: 400;
    color: var(--paper);
    line-height: 1;
  }
  .author-role {
    position: absolute;
    left: 171px;
    top: 1141px;
    margin: 0;
    font-family: "Lato", "Helvetica", sans-serif;
    font-weight: 300;
    font-size: 19px;
    color: var(--paper);
    line-height: 1;
  }
</style>
</head>
<body>
  <main class="cover">
    <svg class="cover-art" viewBox="0 0 900 1200" xmlns="http://www.w3.org/2000/svg">
      <defs>
        <linearGradient id="dusk-fade" x1="0" y1="0" x2="0" y2="1">
          <stop offset="0" stop-color="#b86e79"/>
          <stop offset="0.76" stop-color="#b86e79"/>
          <stop offset="0.94" stop-color="#000000"/>
          <stop offset="1" stop-color="#000000"/>
        </linearGradient>
      </defs>
      <rect class="landscape" x="0" y="0" width="900" height="420" fill="url(#dusk-fade)"
            role="img" aria-label="Silhouette of a mountain ridge against a rose dusk sky"/>
      <g class="bestseller-badge">
        <circle cx="788" cy="88" r="130" fill="var(--gold)"/>
        <circle cx="788" cy="88" r="119" fill="none" stroke="var(--rose)" stroke-width="3"/>
      </g>
      <text class="title-line" x="50" y="560" font-size="86" textLength="802" lengthAdjust="spacingAndGlyphs">LANTERNS UNDER</text>
      <text class="title-word" x="38" y="910" font-size="478" textLength="868" lengthAdjust="spacingAndGlyphs">RAIN</text>
    </svg>
    <p class="author">Marisol Okafor-Reyes</p>
    <p class="author-role">Author</p>
  </main>
</body>
</html>
```